Removals & Storage a5 brochure required

We require a a4 1 fold into a5 brochure designed. we are an established removals and storage company based in southport, uk. we are looking for somthing we can take into more corporate offices ( estate agents etc) to show off what we do. our website has alot of information : www.haul-and-keep.co.uk which may be of use. we offer Domestic and Commercial removals & storage, packaging sales and services, 24/7 self storage options, mobile self storage. archive storage etc etc i have many files like logos etc where required. nice clean images / hgv with our image superimposed
Corporate, estate agents, domestic removals,
Designer to choose colors to be used in the design.

```html
<!DOCTYPE html>
<html lang="en">
<head>
<meta charset="utf-8">
<title>Coastline Removals and Storage – A5 Brochure</title>
<link rel="stylesheet" href="https://fonts.googleapis.com/css2?family=Oswald:wght@500;600;700&family=Roboto:wght@400;500&display=swap">
<style>
  :root{
    --yellow:#f5b512;
    --black:#141414;
    --charcoal:#2a2a2a;
    --slate:#8d9496;
    --paper:#ffffff;
    --bg:#e4e4e4;
    --text:#5a5a5a;
    --photo-warm:#b58a62;
    --photo-light:#d9cbbb;
    --photo-room:#8f7f73;
  }
  *{box-sizing:border-box;margin:0;padding:0}
  html,body{width:1200px;height:900px;overflow:hidden}
  body{background:var(--bg);font-family:"Roboto",Arial,sans-serif;position:relative}

  .page{position:absolute;top:195px;height:509px;background:var(--paper);overflow:hidden;box-shadow:0 6px 18px rgba(0,0,0,.18)}

  /* ---------- Front cover ---------- */
  .cover{left:40px;width:360px;background:var(--black)}
  .cover__sky{position:absolute;inset:0 0 auto 0;height:230px;background:radial-gradient(ellipse at 55% 35%,#3a3a3a 0%,#1a1a1a 60%,#0e0e0e 100%)}
  .cover__shape{position:absolute;left:0;top:0}
  .brand{position:absolute;left:62px;top:98px;display:flex;align-items:center;gap:12px}
  .brand__mark{width:34px;height:34px;background:var(--yellow)}
  .brand__name{font-family:"Oswald",Arial,sans-serif;font-weight:600;color:#fff;font-size:24px;line-height:1.02;text-transform:uppercase;letter-spacing:.5px}
  .cover__band{position:absolute;left:0;top:188px;width:360px;height:30px;background:var(--yellow);display:flex;align-items:center;justify-content:center;font-family:"Oswald",Arial,sans-serif;font-weight:700;font-size:19px;color:var(--black);letter-spacing:.3px;text-transform:uppercase}
  .photo{position:absolute}
  .photo--house{left:0;top:226px;width:128px;height:120px;background:linear-gradient(160deg,#b4806a,#6d4a3a 70%,#8a7a6a);clip-path:polygon(0 0,100% 0,82% 100%,0 82%)}
  .photo--office{left:0;top:352px;width:112px;height:112px;background:linear-gradient(170deg,#cfc8c0,#8b7565 60%,#3d3d3d);clip-path:polygon(0 0,70% 12%,100% 100%,0 100%)}
  .photo--boxes{left:112px;top:222px;width:248px;height:238px;background:linear-gradient(150deg,var(--photo-light) 0%,#e6b27a 40%,var(--photo-warm) 75%,#c9a47e 100%);clip-path:polygon(18% 0,100% 0,100% 100%,0 100%,10% 55%)}
  .cover__url{position:absolute;left:0;top:462px;width:360px;height:34px;background:var(--yellow);display:flex;align-items:center;justify-content:center;font-family:"Roboto",Arial,sans-serif;font-size:16px;letter-spacing:2px;color:var(--black)}

  /* ---------- Inside spread ---------- */
  .spread{left:440px;width:720px}
  .spread__fold{position:absolute;left:360px;top:0;width:1px;height:100%;background:linear-gradient(#e8e8e8,#d0d0d0,#e8e8e8)}
  .spread__base{position:absolute;left:0;bottom:10px;width:100%;height:4px;background:var(--yellow)}
  .tab{position:absolute;height:20px;padding:0 22px 0 10px;background:var(--yellow);clip-path:polygon(0 0,100% 0,calc(100% - 10px) 100%,0 100%);font-family:"Oswald",Arial,sans-serif;font-weight:600;font-size:12px;line-height:20px;color:var(--black)}
  .copy{position:absolute;font-size:8.2px;line-height:1.45;color:var(--text);text-align:justify}
  .copy p+p{margin-top:7px}

  .intro__tab{left:18px;top:22px}
  .intro__copy{left:22px;top:56px;width:318px}
  .intro__photo{position:absolute;left:0;top:196px;width:360px;height:313px;background:linear-gradient(135deg,#e9e3dc 0%,var(--photo-room) 45%,#c7a27c 70%,#b33a30 92%);clip-path:polygon(0 0,100% 55%,100% 100%,0 100%)}
  .intro__edge{position:absolute;left:0;top:0}

  .services__tab{left:380px;top:104px}
  .services__list{position:absolute;left:392px;top:134px;list-style:none;font-size:8.4px;line-height:1.5;color:var(--text)}
  .services__list li{position:relative;padding-left:18px}
  .services__list li::before{content:"";position:absolute;left:0;top:3px;border-left:6px solid var(--yellow);border-top:3.5px solid transparent;border-bottom:3.5px solid transparent}

  .quotes__tab{left:380px;top:290px}
  .quotes__copy{left:392px;top:320px;width:310px}
  .pro__tab{left:380px;top:362px}
  .pro__copy{left:392px;top:392px;width:310px}
</style>
</head>
<body>

  <section class="page cover" aria-label="Front cover">
    <div class="cover__sky"></div>
    <svg class="cover__shape" width="360" height="230" viewBox="0 0 360 230" aria-hidden="true">
      <polygon points="205,0 360,0 360,14 225,14" fill="var(--yellow)"/>
      <polygon points="225,14 360,14 360,22 232,22" fill="var(--slate)"/>
      <polygon points="0,178 360,150 360,188 0,188" fill="var(--slate)"/>
    </svg>
    <div class="brand">
      <span class="brand__mark"></span>
      <span class="brand__name">Crowther<br>Removals &amp; Storage</span>
    </div>
    <div class="cover__band">Coastline Removals and Storage</div>
    <div class="photo photo--house" role="img" aria-label="Photo of a couple carrying boxes outside a brick house"></div>
    <div class="photo photo--office" role="img" aria-label="Photo of an office with desks and chairs"></div>
    <div class="photo photo--boxes" role="img" aria-label="Photo of cardboard boxes and cushions on moving day"></div>
    <div class="cover__url">www.haul-and-keep.co.uk</div>
  </section>

  <section class="page spread" aria-label="Inside spread">
    <div class="tab intro__tab">Coastline Removals and Storage</div>
    <div class="copy intro__copy">
      <p>Coastline Removals and Storage provides seamless house removal and commercial business moves throughout the North west and nationwide.</p>
      <p>With more than two decades of experience within the moving and storage industry, Coastline Removals and Storage provides a reliable, efficient service, ensuring our customers receive a quality service every time.</p>
      <p>In addition to our home, business and office removals we also provide other services such as storage solutions, packing services, antique and piano transportation.</p>
    </div>
    <div class="intro__photo" role="img" aria-label="Photo of removal men moving furniture, boxes and a red suitcase"></div>
    <svg class="intro__edge" width="360" height="509" viewBox="0 0 360 509" aria-hidden="true">
      <polygon points="0,190 360,362 360,372 0,200" fill="var(--yellow)"/>
    </svg>

    <div class="spread__fold"></div>

    <div class="tab services__tab">Services</div>
    <ul class="services__list">
      <li>Domestic removals</li>
      <li>Commercial relocations</li>
      <li>Worldwide shipping management</li>
      <li>Part loads nationwide</li>
      <li>Specialist antique, piano and heavy item transportation</li>
      <li>Domestic and commercial storage</li>
      <li>Dismantling and reassembling of furniture</li>
      <li>Full / Part packing / unpacking services</li>
      <li>Boxes and packaging materials</li>
      <li>Clearance, collection and disposal services</li>
      <li>Courier service</li>
    </ul>

    <div class="tab quotes__tab">FREE Quotations</div>
    <div class="copy quotes__copy">
      <p>Whether you require storage, domestic / commercial removals or would like more details about our services. We can provide a FREE no obligation quotation.</p>
    </div>

    <div class="tab pro__tab">Professional Service</div>
    <div class="copy pro__copy">
      <p>Coastline Removals and Storage are fully insured, holding a commercial insurance policy with leading insurance brokers.</p>
      <p>Our insurance covers Goods in Transit, Warehousing, Employers Liability, Public Liability and our Commercial Vehicle Insurance.</p>
    </div>

    <div class="spread__base"></div>
  </section>

</body>
</html>
```